Domain Parking page and Listing page

1)
In need a design of a domain parking page, mainly with the same features as VORIQ.com as can be seen here: https://wanderplum.com/

2)
I need a design of a website with all domains listed. There's no company logo/name yet so it should be in plain font, for example "tilmorex.site" (this is just an example), similar as:
https://voriq.com/search?&terms=park&results=50&order_by=relevance

Delivery after approval in HTML/CSS. Should be responsive. Ideally use a framework like Bootstrap

Target Market(s)

Domain buyers, business owners

Industry/Entity Type

Business to business, Marketing, domains

Coding

Coded - Design and coding required

Number of Pages Required

2 page

Font styles to use
Sans Serif

Requirements
Must have
• Responsive design, worldly design.

```html
<!DOCTYPE html>
<html lang="en">
<head>
<meta charset="utf-8">
<title>tilmorex.site – Domain name search</title>
<link href="https://fonts.googleapis.com/css2?family=Poppins:wght@400;500;600;700&display=swap" rel="stylesheet">
<style>
:root{
  --hero-dark:#063a33;
  --hero-mid:#0d5a52;
  --green:#5aa55b;
  --green-check:#4caf50;
  --ink:#2b2b2b;
  --muted:#777;
  --line:#e2e2e2;
  --chip:#4a4a4a;
  --teal-link:#7fb3c0;
  --btn-dark:#5f5f5f;
  --btn-light:#e0e0e0;
  --off-bg:#d8f7f3;--off-ink:#1aa6a0;
  --reg-bg:#e5e5e5;--reg-ink:#555;
  --prem-bg:#e1efff;--prem-ink:#2b7bd6;
  --foot:#1f8a5f;
  --foot-dark:#17704d;
}
*{box-sizing:border-box;margin:0;padding:0}
html,body{width:737px;height:1200px;overflow:hidden;background:#fff}
body{font-family:'Poppins',sans-serif;color:var(--ink)}
.page{position:absolute;left:0;top:0;width:1440px;height:2345px;transform:scale(.51181);transform-origin:0 0;overflow:hidden}
.abs{position:absolute}

/* hero */
.hero{position:absolute;left:0;top:0;width:1440px;height:470px;background:radial-gradient(ellipse at 30% 55%,#1a7a72 0%,var(--hero-mid) 30%,var(--hero-dark) 75%)}
.hero-curve{position:absolute;left:0;top:380px}
.brand{position:absolute;display:flex;align-items:center;gap:10px;font-weight:500;font-size:20px;color:#fff}
.brand-mark{width:26px;height:26px;border-radius:5px;background:#9fe0c9}
.nav-links{position:absolute;left:398px;top:26px;display:flex;gap:30px;font-size:16px;color:#e6f2ef}
.btn-login,.btn-signup{position:absolute;top:19px;height:36px;font-size:16px;display:flex;align-items:center;justify-content:center;border-radius:2px}
.btn-login{left:1112px;width:91px;border:1px solid #fff;color:#fff}
.btn-signup{left:1214px;width:110px;background:#fff;color:#0e6d58;font-weight:500}
.nav-rule{position:absolute;left:117px;top:67px;width:1206px;height:1px;background:rgba(255,255,255,.35)}
.eyebrow{position:absolute;top:188px;width:1440px;text-align:center;color:#fff;font-size:22px;font-weight:500}
.headline{position:absolute;top:222px;width:1440px;text-align:center;color:#fff;font-size:44px;font-weight:700}
.search{position:absolute;left:357px;top:305px;width:726px;height:62px;background:#fff;border-radius:31px;display:flex;align-items:center;padding-left:30px;font-size:16px;color:#8a8a8a}
.search-btn{position:absolute;right:0;top:0;width:157px;height:62px;border-radius:31px;background:var(--green);color:#fff;font-size:19px;font-weight:600;display:flex;align-items:center;justify-content:center;gap:14px}
.transfer{position:absolute;top:383px;width:1440px;text-align:center;color:#fff;font-size:16px}
.transfer u{color:#d7f0ea}

/* filters row */
.chip{position:absolute;left:155px;top:559px;width:89px;height:40px;border-radius:20px;background:var(--chip);color:#fff;font-size:17px;font-weight:500;display:flex;align-items:center;justify-content:center;gap:6px}
.clear{position:absolute;left:271px;top:568px;font-size:16px;color:var(--teal-link)}
.suggested{position:absolute;left:616px;top:568px;font-size:16px;font-weight:600}
.select{position:absolute;border:1px solid #999;display:flex;align-items:center;justify-content:space-between;padding:0 16px;font-size:16px}
.relevance{left:1007px;top:555px;width:214px;height:48px;font-weight:600;border-color:#777}
.caret{width:0;height:0;border-left:4px solid transparent;border-right:4px solid transparent;border-top:5px solid #333}

/* results panel */
.panel{position:absolute;left:119px;top:628px;width:1202px;height:1100px;border:1px solid #ddd;border-radius:14px}
.sidebar-rule{position:absolute;left:529px;top:629px;width:1px;height:1122px;background:#e6e6e6}
.f-title{position:absolute;left:155px;font-size:16px;font-weight:600}
.f-input{position:absolute;height:48px;width:110px;border:1px solid #ddd;display:flex;align-items:center;padding-left:16px;font-size:16px}
.f-input.wide{width:271px;color:#aaa}
.f-to{position:absolute;left:283px;font-size:16px}
.slider{position:absolute;left:155px;width:271px;height:2px;background:#ddd}
.slider i{position:absolute;top:0;height:2px;background:var(--green)}
.slider b{position:absolute;top:-4px;width:10px;height:10px;border-radius:50%;background:var(--green)}
.check{position:absolute;left:155px;display:flex;align-items:center;gap:10px;font-size:14px}
.box{width:19px;height:19px;border:1.5px solid #999;border-radius:3px;display:flex;align-items:center;justify-content:center}
.box.on{background:var(--green-check);border-color:var(--green-check)}
.more-ext{left:155px;top:1108px;width:271px;height:48px;border-color:#ddd}

.col-head{position:absolute;top:660px;font-size:14px}
.row{position:absolute;left:530px;width:788px;height:80px;border-top:1px solid #e6e6e6;display:flex;align-items:center}
.domain{position:absolute;left:48px;display:flex;align-items:center;gap:12px;font-size:19px;font-weight:500}
.tag{font-size:13px;padding:2px 6px;border-radius:3px;font-weight:400}
.tag.off{background:var(--off-bg);color:var(--off-ink)}
.tag.reg{background:var(--reg-bg);color:var(--reg-ink)}
.tag.prem{background:var(--prem-bg);color:var(--prem-ink)}
.price{position:absolute;right:214px;font-size:17px}
.action{position:absolute;left:599px;width:145px;height:44px;border-radius:3px;display:flex;align-items:center;justify-content:center;gap:10px;font-size:16px;font-weight:600}
.action.cart{background:var(--btn-dark);color:#fff}
.action.offer{background:var(--btn-light);color:#7b7b7b}
.rows-end{position:absolute;left:530px;top:1578px;width:791px;height:1px;background:#e6e6e6}
.pager{position:absolute;left:720px;top:1627px;display:flex;align-items:center;gap:0;font-size:17px}
.pg{width:28px;height:28px;display:flex;align-items:center;justify-content:center;border-radius:3px}

/* footer */
.footer{position:absolute;left:0;top:1830px;width:1440px;height:515px}
.foot-bg{position:absolute;left:0;top:0}
.foot-text{position:absolute;color:#fff}
.foot-h{position:absolute;top:1944px;color:#fff;font-size:15px;font-weight:600}
.foot-list{position:absolute;top:1986px;list-style:none;color:#e8f5ee;font-size:16px;line-height:28px}
.social{position:absolute;left:1075px;top:1984px;display:flex;gap:8px}
.social span{width:30px;height:30px;border-radius:4px;background:rgba(255,255,255,.35)}
.lang{position:absolute;left:1078px;top:2041px;color:#fff;font-size:16px;font-weight:500;border-bottom:1px solid #fff;padding-right:20px;display:flex;align-items:center;gap:10px}
.lang .caret{border-top-color:#fff}
.foot-rule{position:absolute;left:151px;top:2159px;width:1153px;height:1px;background:rgba(255,255,255,.45)}
</style>
</head>
<body>
<div class="page">

  <header class="hero" role="img" aria-label="Dark teal night view of the earth with glowing network arcs"></header>
  <svg class="hero-curve" width="1440" height="100" viewBox="0 380 1440 100"><path d="M0 393 Q720 527 1440 393 L1440 480 L0 480Z" fill="#fff"/></svg>

  <div class="brand" style="left:115px;top:21px"><span class="brand-mark"></span>tilmorex.site</div>
  <nav class="nav-links"><span>Auction</span><span>Buy Domain</span><span>Sell Domain</span><span>Learn</span><span>Contact Us</span></nav>
  <div class="btn-login">Login</div>
  <div class="btn-signup">Sign Up</div>
  <div class="nav-rule"></div>

  <p class="eyebrow">DOMAIN NAME SEARCH</p>
  <h1 class="headline">It all starts with a great domain</h1>
  <div class="search">Find your new domain name
    <div class="search-btn">Check <svg width="10" height="16" viewBox="0 0 10 16"><path d="M2 2l6 6-6 6" stroke="#fff" stroke-width="2" fill="none"/></svg></div>
  </div>
  <p class="transfer">Is your domain name with a different registrar? <u>Transfer it today</u></p>

  <div class="chip">park <svg width="11" height="11" viewBox="0 0 11 11"><path d="M1 1l9 9M10 1l-9 9" stroke="#fff" stroke-width="2"/></svg></div>
  <div class="clear">Clear (1)</div>
  <div class="suggested">Suggested names</div>
  <div class="select relevance">Relevance <span class="caret"></span></div>

  <section class="panel"></section>
  <div class="sidebar-rule"></div>

  <!-- filters -->
  <div class="f-title" style="top:661px">Price Range</div>
  <div class="f-input" style="left:155px;top:699px">$ 0</div>
  <div class="f-to" style="top:712px">to</div>
  <div class="f-input" style="left:316px;top:699px">$ 200,000</div>
  <div class="slider" style="top:766px"><i style="left:4px;width:105px"></i><b style="left:0"></b><b style="left:104px"></b></div>

  <div class="f-title" style="top:803px">Options</div>
  <div class="check" style="top:841px"><span class="box on"><svg width="12" height="10" viewBox="0 0 12 10"><path d="M1 5l3.5 3.5L11 1" stroke="#fff" stroke-width="2" fill="none"/></svg></span>Popular domain names</div>
  <div class="check" style="top:876px"><span class="box"></span>3-letter domain names</div>
  <div class="check" style="top:911px"><span class="box"></span>Premium domain name</div>

  <div class="f-title" style="top:963px">Extensions</div>
  <div class="check" style="top:1001px"><span class="box"></span>.com</div>
  <div class="check" style="top:1036px"><span class="box on"><svg width="12" height="10" viewBox="0 0 12 10"><path d="M1 5l3.5 3.5L11 1" stroke="#fff" stroke-width="2" fill="none"/></svg></span>.net</div>
  <div class="check" style="top:1071px"><span class="box"></span>.org</div>
  <div class="select more-ext">More extensions <span class="caret"></span></div>

  <div class="f-title" style="top:1187px">Length</div>
  <div class="f-input" style="left:155px;top:1225px">1</div>
  <div class="f-to" style="top:1238px">to</div>
  <div class="f-input" style="left:316px;top:1225px">25</div>
  <div class="slider" style="top:1292px"><i style="left:4px;width:185px"></i><b style="left:0"></b><b style="left:184px"></b></div>

  <div class="f-title" style="top:1329px">Name</div>
  <div class="check" style="top:1367px"><span class="box"></span>No hyphens (-)</div>
  <div class="check" style="top:1402px"><span class="box"></span>No numerals (0-9)</div>
  <div class="check" style="top:1437px"><span class="box"></span>Premium domain name</div>

  <div class="f-title" style="top:1489px">Starting with</div>
  <div class="f-input wide" style="left:155px;top:1527px">Type here</div>
  <div class="f-title" style="top:1606px">Ending with</div>
  <div class="f-input wide" style="left:155px;top:1644px">Type here</div>

  <!-- results -->
  <div class="col-head" style="left:577px">Domain&nbsp; name</div>
  <div class="col-head" style="left:994px">Pricing</div>

  <div class="row" style="top:698px"><div class="domain">park.amsterdam <span class="tag off">20% OFF</span></div><div class="price">$27,000/year</div><div class="action cart"><svg width="20" height="18" viewBox="0 0 20 18"><path d="M1 1h3l2.5 10h10L19 4H5.5M8 16a1 1 0 100-.1M15 16a1 1 0 100-.1" stroke="#fff" stroke-width="1.6" fill="none"/></svg>Add to cart</div></div>
  <div class="row" style="top:778px"><div class="domain">park.frl <span class="tag reg">REGISTERED IN 2016</span></div><div class="action offer"><svg width="20" height="20" viewBox="0 0 20 20"><circle cx="10" cy="10" r="8.5" stroke="#888" stroke-width="1.5" fill="none"/><text x="10" y="14" font-size="11" text-anchor="middle" fill="#888" font-family="Poppins,sans-serif">$</text></svg>Make offer</div></div>
  <div class="row" style="top:858px"><div class="domain">park.com.ar <span class="tag prem">PREMIUM</span></div><div class="price">$27,000/year</div><div class="action cart"><svg width="20" height="18" viewBox="0 0 20 18"><path d="M1 1h3l2.5 10h10L19 4H5.5M8 16a1 1 0 100-.1M15 16a1 1 0 100-.1" stroke="#fff" stroke-width="1.6" fill="none"/></svg>Add to cart</div></div>
  <div class="row" style="top:938px"><div class="domain">park.com.cn <span class="tag reg">REGISTERED IN 2016</span></div><div class="action offer"><svg width="20" height="20" viewBox="0 0 20 20"><circle cx="10" cy="10" r="8.5" stroke="#888" stroke-width="1.5" fill="none"/><text x="10" y="14" font-size="11" text-anchor="middle" fill="#888" font-family="Poppins,sans-serif">$</text></svg>Make offer</div></div>
  <div class="row" style="top:1018px"><div class="domain">park.frl <span class="tag reg">REGISTERED IN 2016</span></div><div class="action offer"><svg width="20" height="20" viewBox="0 0 20 20"><circle cx="10" cy="10" r="8.5" stroke="#888" stroke-width="1.5" fill="none"/><text x="10" y="14" font-size="11" text-anchor="middle" fill="#888" font-family="Poppins,sans-serif">$</text></svg>Make offer</div></div>
  <div class="row" style="top:1098px"><div class="domain">park.com.ar <span class="tag off">20% OFF</span></div><div class="price">$9,000/year</div><div class="action cart"><svg width="20" height="18" viewBox="0 0 20 18"><path d="M1 1h3l2.5 10h10L19 4H5.5M8 16a1 1 0 100-.1M15 16a1 1 0 100-.1" stroke="#fff" stroke-width="1.6" fill="none"/></svg>Add to cart</div></div>
  <div class="row" style="top:1178px"><div class="domain">park.fit <span class="tag off">20% OFF</span></div><div class="price">$9,000/year</div><div class="action cart"><svg width="20" height="18" viewBox="0 0 20 18"><path d="M1 1h3l2.5 10h10L19 4H5.5M8 16a1 1 0 100-.1M15 16a1 1 0 100-.1" stroke="#fff" stroke-width="1.6" fill="none"/></svg>Add to cart</div></div>
  <div class="row" style="top:1258px"><div class="domain">park.com.ar <span class="tag prem">PREMIUM</span></div><div class="price">$19,000/year</div><div class="action cart"><svg width="20" height="18" viewBox="0 0 20 18"><path d="M1 1h3l2.5 10h10L19 4H5.5M8 16a1 1 0 100-.1M15 16a1 1 0 100-.1" stroke="#fff" stroke-width="1.6" fill="none"/></svg>Add to cart</div></div>
  <div class="row" style="top:1338px"><div class="domain">park.fit <span class="tag prem">PREMIUM</span></div><div class="price">$27,000/year</div><div class="action cart"><svg width="20" height="18" viewBox="0 0 20 18"><path d="M1 1h3l2.5 10h10L19 4H5.5M8 16a1 1 0 100-.1M15 16a1 1 0 100-.1" stroke="#fff" stroke-width="1.6" fill="none"/></svg>Add to cart</div></div>
  <div class="row" style="top:1418px"><div class="domain">park.fit <span class="tag off">20% OFF</span></div><div class="price">$9,000/year</div><div class="action cart"><svg width="20" height="18" viewBox="0 0 20 18"><path d="M1 1h3l2.5 10h10L19 4H5.5M8 16a1 1 0 100-.1M15 16a1 1 0 100-.1" stroke="#fff" stroke-width="1.6" fill="none"/></svg>Add to cart</div></div>
  <div class="row" style="top:1498px"><div class="domain">park.frl <span class="tag reg">REGISTERED IN 2016</span></div><div class="action offer"><svg width="20" height="20" viewBox="0 0 20 20"><circle cx="10" cy="10" r="8.5" stroke="#888" stroke-width="1.5" fill="none"/><text x="10" y="14" font-size="11" text-anchor="middle" fill="#888" font-family="Poppins,sans-serif">$</text></svg>Make offer</div></div>
  <div class="rows-end"></div>

  <div class="pager">
    <span class="pg" style="background:#eee"><svg width="8" height="12" viewBox="0 0 8 12"><path d="M6 1L1 6l5 5" stroke="#bbb" stroke-width="1.6" fill="none"/></svg></span>
    <span class="pg" style="margin-left:8px;color:var(--green)">1</span>
    <span class="pg" style="margin-left:8px">2</span>
    <span class="pg" style="margin-left:8px">3</span>
    <span class="pg" style="margin-left:8px">...</span>
    <span class="pg" style="margin-left:12px">22</span>
    <span class="pg" style="margin-left:8px;background:#dff5df"><svg width="8" height="12" viewBox="0 0 8 12"><path d="M2 1l5 5-5 5" stroke="#3c9a3e" stroke-width="1.8" fill="none"/></svg></span>
  </div>

  <!-- footer -->
  <footer class="footer">
    <svg class="foot-bg" width="1440" height="515" viewBox="0 0 1440 515">
      <defs><linearGradient id="fg" x1="0" y1="0" x2="1" y2="0"><stop offset="0" stop-color="#17704d"/><stop offset="1" stop-color="#24915f"/></linearGradient></defs>
      <path d="M0 80 Q720 -80 1440 80 L1440 515 L0 515Z" fill="url(#fg)"/>
      <circle cx="1440" cy="350" r="250" fill="none" stroke="rgba(255,255,255,.06)" stroke-width="40"/>
    </svg>
  </footer>
  <div class="brand" style="left:146px;top:1944px"><span class="brand-mark"></span>tilmorex.site</div>
  <div class="abs" style="left:146px;top:1989px;width:69px;height:1px;background:rgba(255,255,255,.5)"></div>
  <p class="foot-text" style="left:146px;top:1998px;width:310px;font-size:13.5px;line-height:21px;color:#e8f5ee">Have questions or need assistance? Reach out to our dedicated support team at</p>
  <div class="foot-text" style="left:146px;top:2058px;font-size:14px;display:flex;gap:10px;align-items:center"><svg width="16" height="12" viewBox="0 0 16 12"><rect x="1" y="1" width="14" height="10" stroke="#fff" stroke-width="1.4" fill="none"/><path d="M1 1l7 5 7-5" stroke="#fff" stroke-width="1.4" fill="none"/></svg><u>help@tilmorex.site</u></div>
  <div class="foot-text" style="left:148px;top:2091px;font-size:14px;display:flex;gap:10px;align-items:center"><svg width="14" height="14" viewBox="0 0 14 14"><path d="M3 1l2.5 3-1.5 1.5c1 2 2.5 3.5 4.5 4.5L10 8.5l3 2.5-1.5 2C6 13 1 8 1 2.5Z" fill="#fff"/></svg>1-800-555-0142.</div>

  <div class="foot-h" style="left:566px">HELP CENTER</div>
  <ul class="foot-list" style="left:566px"><li>Help centre</li><li>FAQ</li><li>Quick Start Guide</li><li>Tutorials</li><li>Associate Blog</li></ul>
  <div class="foot-h" style="left:813px">MY ACCOUNT</div>
  <ul class="foot-list" style="left:813px"><li>Manage Accounts</li><li>How to Withdraw</li><li>Account Varification</li><li>Safety &amp; Security</li><li>Membership Level</li></ul>
  <div class="foot-h" style="left:1075px">FOLLOW US</div>
  <div class="social"><span></span><span></span><span></span><span></span></div>
  <div class="lang">English <span class="caret"></span></div>

  <div class="foot-rule"></div>
  <p class="foot-text" style="left:0;top:2181px;width:1440px;text-align:center;font-size:16px">Copyright © 2019.All Rights Reserved By tilmorex.site</p>
  <p class="foot-text" style="left:149px;top:2240px;font-size:16px;font-weight:600">Disclaimer</p>
  <p class="foot-text" style="left:146px;top:2273px;width:1160px;font-size:14px;line-height:21px;color:#eef8f2">The information provided on this page is for informational purposes only and does not constitute legal or financial advice. All domain sales are subject to applicable terms and conditions. Prices and availability are subject to change without notice.</p>

</div>
</body>
</html>
```